Business card por a urban DJ, up scale audience target

Need a sober design, modern, conservative colors but i can consider some options, y play rnb, hip hop, EDM and top40.

Business card for contact and personal info, double sided, use logo attrached please; im 42 so i need a card acording to my age an target audience.

Target Market(s)

Adult people, up scale audience

Industry/Entity Type

Music Download

Contact Information for Business Card

Cel (574) 3209415586 www.lumaverso.com

Requirements
Must have
• open mind
Nice to have
• open mind
Should not have
• DJ

```html
<!DOCTYPE html>
<html lang="en">
<head>
<meta charset="utf-8">
<title>LUMA Business Card</title>
<link rel="stylesheet" href="https://fonts.googleapis.com/css2?family=Open+Sans:wght@400;700;800&display=swap">
<style>
  :root {
    --stage: #2b2b2b;
    --card-dark: #050505;
    --card-light: #ffffff;
    --logo-grey: #a8a8aa;
    --bar-dark: #1b1b1b;
    --bar-light: #e8e8e8;
    --ink: #111111;
    --ink-soft: #444444;
  }
  * { margin: 0; padding: 0; box-sizing: border-box; }
  html, body {
    width: 1200px; height: 900px; overflow: hidden;
    background: var(--stage);
    font-family: "Open Sans", Arial, sans-serif;
  }
  .card {
    position: absolute;
    width: 560px; height: 320px;
    overflow: hidden;
    box-shadow: 0 14px 30px rgba(0,0,0,.45);
  }
  .card-front { left: 90px; top: 110px; background: var(--card-dark); }
  .card-back { left: 550px; top: 450px; background: var(--card-light); }
  .level-bars { position: absolute; left: 0; bottom: 0; width: 100%; height: 100%; }
  .brand {
    position: absolute;
    display: flex; align-items: center; gap: 14px;
    font-weight: 800; letter-spacing: 4px; line-height: 1;
  }
  .card-front .brand {
    left: 150px; top: 95px; font-size: 96px; color: var(--logo-grey);
  }
  .card-front .brand-square { width: 22px; height: 22px; background: var(--logo-grey); }
  .card-back .brand {
    left: 40px; top: 140px; font-size: 70px; color: var(--ink);
  }
  .card-back .brand-square { width: 16px; height: 16px; background: var(--ink); }
  .contact {
    position: absolute; left: 330px; top: 48px; color: var(--ink);
  }
  .contact-name { font-size: 22px; font-weight: 700; }
  .contact-role { font-size: 13px; color: var(--ink-soft); margin: 2px 0 8px; }
  .contact-line {
    display: flex; align-items: center; gap: 8px;
    font-size: 14px; color: var(--ink-soft); margin-bottom: 3px;
  }
  .contact-line svg { width: 11px; height: 11px; flex: none; }
</style>
</head>
<body>

<section class="card card-front" aria-label="Card front">
  <svg class="level-bars" viewBox="0 0 560 320" aria-hidden="true" fill="var(--bar-dark)">
    <rect x="190" y="250" width="14" height="70"/>
    <rect x="212" y="232" width="14" height="88"/>
    <rect x="234" y="262" width="14" height="58"/>
    <rect x="256" y="220" width="14" height="100"/>
    <rect x="278" y="244" width="14" height="76"/>
    <rect x="300" y="206" width="14" height="114"/>
    <rect x="322" y="230" width="14" height="90"/>
    <rect x="344" y="190" width="14" height="130"/>
    <rect x="366" y="214" width="14" height="106"/>
    <rect x="388" y="168" width="14" height="152"/>
    <rect x="410" y="196" width="14" height="124"/>
    <rect x="432" y="150" width="14" height="170"/>
    <rect x="454" y="176" width="14" height="144"/>
    <rect x="476" y="120" width="14" height="200"/>
    <rect x="498" y="146" width="14" height="174"/>
    <rect x="520" y="90" width="14" height="230"/>
    <rect x="542" y="112" width="14" height="208"/>
  </svg>
  <div class="brand"><span class="brand-square"></span>LUMA</div>
</section>

<section class="card card-back" aria-label="Card back">
  <svg class="level-bars" viewBox="0 0 560 320" aria-hidden="true" fill="var(--bar-light)">
    <rect x="4" y="262" width="14" height="58"/>
    <rect x="26" y="240" width="14" height="80"/>
    <rect x="48" y="270" width="14" height="50"/>
    <rect x="70" y="250" width="14" height="70"/>
    <rect x="92" y="232" width="14" height="88"/>
    <rect x="114" y="258" width="14" height="62"/>
    <rect x="136" y="236" width="14" height="84"/>
    <rect x="158" y="214" width="14" height="106"/>
    <rect x="180" y="244" width="14" height="76"/>
    <rect x="202" y="222" width="14" height="98"/>
    <rect x="224" y="248" width="14" height="72"/>
    <rect x="246" y="226" width="14" height="94"/>
    <rect x="268" y="204" width="14" height="116"/>
    <rect x="290" y="232" width="14" height="88"/>
    <rect x="312" y="210" width="14" height="110"/>
    <rect x="334" y="190" width="14" height="130"/>
    <rect x="356" y="220" width="14" height="100"/>
    <rect x="378" y="196" width="14" height="124"/>
    <rect x="400" y="176" width="14" height="144"/>
    <rect x="422" y="200" width="14" height="120"/>
    <rect x="444" y="160" width="14" height="160"/>
    <rect x="466" y="184" width="14" height="136"/>
    <rect x="488" y="144" width="14" height="176"/>
    <rect x="510" y="170" width="14" height="150"/>
    <rect x="532" y="130" width="14" height="190"/>
  </svg>
  <div class="brand"><span class="brand-square"></span>LUMA</div>
  <div class="contact">
    <p class="contact-name">Marco Vell</p>
    <p class="contact-role">CEO</p>
    <p class="contact-line">
      <svg viewBox="0 0 12 12" aria-hidden="true"><rect x="3" y="0.5" width="6" height="11" rx="1" fill="none" stroke="#444" stroke-width="1.2"/><rect x="5" y="9" width="2" height="1" fill="#444"/></svg>
      (574) 3209415586
    </p>
    <p class="contact-line">
      <svg viewBox="0 0 12 12" aria-hidden="true"><circle cx="6" cy="6" r="5.2" fill="none" stroke="#444" stroke-width="1.1"/><ellipse cx="6" cy="6" rx="2.3" ry="5.2" fill="none" stroke="#444" stroke-width="1"/><line x1="0.8" y1="6" x2="11.2" y2="6" stroke="#444" stroke-width="1"/></svg>
      www.lumaverso.com
    </p>
  </div>
</section>

</body>
</html>
```